New Business Card Design Project

Hi! I would like for you to design a business card for our aesthetic injections business. We offer Velmo, filler, skin care. I would like it to be elegant, feminine, modern and sleek/clean. I like black/gold foil/ivory/parchment colors. It can be either one or two sided. I would like matte black with gold foil logo on one side and ivory with gold foil information on the other side

Target Market(s)

target market is the discerning woman who wants to look her best

Industry/Entity Type

beauty

Contact Information for Business Card

logo, name, phone, email, website, instagram, facebook, location

Requirements
Must have
• logo and info
Nice to have
• the icons for cell, instagram, email, fb etc
Should not have
• images of people

```html
<!DOCTYPE html>
<html lang="en">
<head>
<meta charset="utf-8">
<title>Velour Lounge Business Card</title>
<link href="https://fonts.googleapis.com/css2?family=Inter:wght@400;500;700&display=swap" rel="stylesheet">
<style>
  :root {
    --backdrop: #d9d3cb;
    --ivory: #ebe5d8;
    --gold: #b27a1c;
    --gold-soft: #c99a4a;
    --white: #fbf7ef;
  }
  * { box-sizing: border-box; margin: 0; padding: 0; }
  html, body {
    width: 1200px; height: 800px; overflow: hidden;
    background: var(--backdrop);
    font-family: "Inter", Arial, sans-serif;
  }
  .stage {
    width: 1200px; height: 800px;
    display: flex; flex-direction: column;
    align-items: center; justify-content: center; gap: 40px;
  }
  .card {
    position: relative;
    width: 560px; height: 320px;
    background: var(--ivory);
    color: var(--gold);
    box-shadow: 0 10px 30px rgba(80, 60, 30, 0.18);
  }
  .brand-mark {
    position: absolute;
    width: 180px; height: 180px;
    border: 1.5px solid var(--gold);
    border-radius: 50%;
    display: flex; align-items: center; justify-content: center;
    text-align: center;
  }
  .card--front .brand-mark { left: 40px; top: 70px; }
  .card--back .brand-mark { left: 190px; top: 70px; }
  .brand-name {
    font-weight: 500; font-size: 22px; line-height: 1.2;
    letter-spacing: 0.04em; color: var(--gold);
  }
  .contact-block {
    position: absolute; left: 262px; top: 62px; right: 0;
  }
  .holder-name {
    font-weight: 700; font-size: 22px; letter-spacing: 0.02em;
  }
  .holder-title {
    font-weight: 500; font-size: 13px; margin-top: 1px;
  }
  .divider {
    height: 1px; background: var(--gold-soft);
    margin: 10px 0 14px;
  }
  .contact-list { list-style: none; }
  .contact-item {
    display: flex; align-items: flex-start; gap: 9px;
    font-weight: 500; font-size: 13px; line-height: 17px;
    margin-bottom: 5px;
  }
  .contact-icon {
    flex: none; width: 15px; height: 15px; margin-top: 1px;
  }
</style>
</head>
<body>
<main class="stage">
  <section class="card card--front" aria-label="Business card front">
    <div class="brand-mark"><span class="brand-name">Velour<br>Lounge</span></div>
    <div class="contact-block">
      <p class="holder-name">ADRIAN HALE</p>
      <p class="holder-title">President</p>
      <div class="divider"></div>
      <ul class="contact-list">
        <li class="contact-item">
          <svg class="contact-icon" viewBox="0 0 16 16"><circle cx="8" cy="8" r="8" fill="var(--gold)"/><path d="M8 3.5a3 3 0 0 0-3 3c0 2.2 3 5.5 3 5.5s3-3.3 3-5.5a3 3 0 0 0-3-3z" fill="var(--white)"/><circle cx="8" cy="6.5" r="1.1" fill="var(--gold)"/></svg>
          <span>4120 Willow Crest Road<br>Juneau, Alaska 99801</span>
        </li>
        <li class="contact-item">
          <svg class="contact-icon" viewBox="0 0 16 16"><circle cx="8" cy="8" r="8" fill="var(--gold)"/><path d="M5.2 4.2l1.5-.3.8 2-1 .8a5.5 5.5 0 0 0 2.8 2.8l.8-1 2 .8-.3 1.5c-4 .5-7.1-2.6-6.6-6.6z" fill="var(--white)"/></svg>
          <span>555-214-7730</span>
        </li>
        <li class="contact-item">
          <svg class="contact-icon" viewBox="0 0 16 16"><circle cx="8" cy="8" r="8" fill="var(--gold)"/><rect x="4" y="5" width="8" height="6" rx="0.8" fill="var(--white)"/><path d="M4.3 5.4L8 8.3l3.7-2.9" fill="none" stroke="var(--gold)" stroke-width="0.9"/></svg>
          <span>hello@velourlounge.com</span>
        </li>
        <li class="contact-item">
          <svg class="contact-icon" viewBox="0 0 16 16"><circle cx="8" cy="8" r="8" fill="var(--gold)"/><circle cx="8" cy="8" r="4" fill="none" stroke="var(--white)" stroke-width="1"/><path d="M4 8h8M8 4c-2 2.4-2 5.6 0 8M8 4c2 2.4 2 5.6 0 8" fill="none" stroke="var(--white)" stroke-width="0.8"/></svg>
          <span>velourlounge.com</span>
        </li>
        <li class="contact-item">
          <svg class="contact-icon" viewBox="0 0 16 16"><circle cx="8" cy="8" r="8" fill="var(--gold)"/></svg>
          <span>/velourlounge</span>
        </li>
        <li class="contact-item">
          <svg class="contact-icon" viewBox="0 0 16 16"><circle cx="8" cy="8" r="8" fill="var(--gold)"/></svg>
          <span>@velourlounge</span>
        </li>
      </ul>
    </div>
  </section>

  <section class="card card--back" aria-label="Business card back">
    <div class="brand-mark"><span class="brand-name">Velour<br>Lounge</span></div>
  </section>
</main>
</body>
</html>
```